Law firm website marketed direct to many individual clients

I need someone to design a very basic website for a law firm that will be very eye catching. It's going to be a single-paged, scrolling website with a small number of folds. I have uploaded a simple word document that outlines the basics of what I thought could be the layout, but I am open to suggestion on font, size, shades of color, organization, etc. etc. Essentially the website just needs to be a very efficient and visually appealing way of conveying some simple messages.

Target Market(s)

High volumes of individuals who have gotten into a car accident and then google on their phones a lawyer to hire to represent them.

Industry/Entity Type

Legal

Number of Pages Required

1 page

Font styles to use
Serif
Sans Serif

Colors
34a7d7
85cae6
0592cd

Requirements
Must have
• Must be bright and grab the users attention with color scheme and layout. The different sections should be done in such a way that they can fit entirely onto one smart phone or tablet screen.
Nice to have
• I'd like to try and see what it looks like if in the middle somewhere there is a fold that says "MEET YOUR ATTORNEYS" and includes individual photos of two attorneys, one on the left side and one on the right. And then a small bio section on them. I don't want the photos to include a square or rectangle background, I want the person in the photo to be superimposed on top of whatever pattern or background you have in the fold.
Should not have
• Do not want too much text. Anything more than 2 sentences in any single place is unacceptable.

```html
<!DOCTYPE html>
<html lang="en">
<head>
<meta charset="utf-8">
<title>Harborline Legal</title>
<link rel="stylesheet" href="https://fonts.googleapis.com/css2?family=Open+Sans:ital,wght@0,400;0,600;0,700;1,400&family=Raleway:ital,wght@0,400;0,600;0,700;1,400;1,500&family=Arimo:wght@400;700&display=swap">
<style>
  :root {
    --blue: #34a7d7;
    --blue-deep: #0592cd;
    --blue-soft: #85cae6;
    --ink: #444444;
    --muted: #8a8a8a;
    --band: #efefef;
    --rule: #dcdcdc;
    --footer: #3d3d3d;
    --white: #ffffff;
  }
  * { margin: 0; padding: 0; box-sizing: border-box; }
  html, body { width: 803px; height: 1200px; overflow: hidden; background: var(--white); }
  body { position: relative; font-family: "Arimo", Arial, sans-serif; color: var(--ink); }
  .abs { position: absolute; }

  /* header */
  .site-header { left: 0; top: 0; width: 803px; height: 70px; background: var(--white); }
  .brand { left: 53px; top: 15px; font-family: "Raleway", sans-serif; font-weight: 400; font-size: 28px; color: var(--blue); letter-spacing: 0.2px; }
  .header-phone { right: 54px; top: 23px; display: flex; align-items: center; gap: 10px; font-family: "Arimo", sans-serif; font-weight: 700; font-size: 19px; color: #555; }

  /* hero */
  .hero { left: 0; top: 70px; width: 803px; height: 383px; overflow: hidden; }
  .hero-photo { position: absolute; inset: 0;
    background:
      radial-gradient(ellipse at 70% 40%, rgba(140,110,85,0.55), transparent 60%),
      radial-gradient(ellipse at 55% 85%, #6a3a1c 0%, transparent 55%),
      linear-gradient(180deg, #4a4440 0%, #5d4a3c 45%, #7a5434 75%, #8a5d38 100%); }
  .hero-shade { position: absolute; inset: 0; background: rgba(30,26,24,0.35); }
  .hero-title { position: absolute; left: 0; top: 110px; width: 100%; text-align: center; font-family: "Open Sans", sans-serif; font-weight: 700; font-size: 59px; letter-spacing: -0.5px; color: var(--white); }
  .hero-title .accent { color: var(--blue); }
  .hero-call { position: absolute; left: 0; top: 191px; width: 100%; text-align: center; font-family: "Arimo", sans-serif; font-size: 29px; color: var(--blue); }
  .hero-call-btn { position: absolute; left: 380px; top: 232px; }

  /* features */
  .features { left: 0; top: 453px; width: 803px; height: 349px; background: var(--band); }
  .feature { position: absolute; top: 32px; width: 160px; }
  .feature svg { display: block; height: 42px; }
  .feature-title { position: absolute; font-family: "Raleway", sans-serif; font-size: 12px; line-height: 14px; color: #333; text-transform: uppercase; }
  .feature-text { position: absolute; font-size: 10.5px; line-height: 14px; color: var(--muted); }
  .divider { position: absolute; top: 36px; width: 1px; height: 108px; background: var(--rule); }
  .rule { left: 53px; top: 178px; width: 700px; height: 2px; background: #e2e2e2; }
  .case-title { left: 0; top: 208px; width: 803px; text-align: center; font-family: "Raleway", sans-serif; font-weight: 700; font-size: 28px; color: var(--blue); }
  .case-call { left: 0; top: 250px; width: 803px; text-align: center; font-family: "Open Sans", sans-serif; font-style: italic; font-size: 25px; color: #555; }
  .learn-more { left: 0; top: 293px; width: 803px; text-align: center; font-family: "Raleway", sans-serif; font-style: italic; font-weight: 600; font-size: 13px; color: var(--blue); text-decoration: underline; }

  /* cards */
  .cards { left: 0; top: 802px; width: 803px; height: 286px; background: var(--white); }
  .card { position: absolute; top: 41px; width: 345px; }
  .card-media { position: relative; height: 119px; display: flex; align-items: center; justify-content: center; text-align: center; }
  .card-media.client { background: linear-gradient(100deg, #4a3330 0%, #7c6a66 45%, #9c8f8a 70%, #6b6766 100%); }
  .card-media.team { background: linear-gradient(180deg, #c9cdd2 0%, #b4b8bd 50%, #6e7075 100%); }
  .card-heading { font-family: "Open Sans", sans-serif; font-weight: 700; font-size: 20px; line-height: 24px; color: var(--white); text-transform: uppercase; text-shadow: 0 1px 3px rgba(0,0,0,0.45); }
  .card-text { margin-top: 14px; padding: 0 2px; font-size: 10.5px; line-height: 17px; color: var(--muted); }
  .cards-call { left: 0; top: 221px; width: 803px; text-align: center; font-family: "Open Sans", sans-serif; font-style: italic; font-size: 25px; color: #555; }
  .cards-call span { color: var(--blue); }

  /* footer */
  .site-footer { left: 0; top: 1088px; width: 803px; height: 112px; background: var(--footer); }
  .footer-label { left: 53px; top: 25px; font-family: "Raleway", sans-serif; font-style: italic; font-size: 13px; color: var(--white); letter-spacing: 0.3px; }
  .footer-ring { width: 35px; height: 35px; border: 1.5px solid var(--blue); border-radius: 50%; display: flex; align-items: center; justify-content: center; }
  .footer-address { left: 97px; top: 50px; font-size: 10.5px; line-height: 17px; color: #c9c9c9; }
  .footer-phone { left: 340px; top: 61px; font-size: 10.5px; color: #c9c9c9; }
  .footer-brand { right: 54px; top: 34px; font-family: "Raleway", sans-serif; font-size: 23px; color: var(--blue); }
  .footer-copy { right: 49px; top: 67px; font-size: 10.5px; color: #a9a9a9; }
  .footer-copy span { color: var(--blue); }
</style>
</head>
<body>

<header class="site-header abs">
  <div class="brand abs">Harborline Legal</div>
  <div class="header-phone abs">
    <svg width="22" height="22" viewBox="0 0 24 24" aria-hidden="true"><path fill="#34a7d7" d="M6.6 10.8a15.1 15.1 0 0 0 6.6 6.6l2.2-2.2c.3-.3.7-.4 1-.2 1.1.4 2.3.6 3.6.6.6 0 1 .4 1 1V20c0 .6-.4 1-1 1A17 17 0 0 1 3 4c0-.6.4-1 1-1h3.5c.6 0 1 .4 1 1 0 1.3.2 2.5.6 3.6.1.3 0 .7-.2 1z"/></svg>
    555-014-2290
  </div>
</header>

<section class="hero abs">
  <div class="hero-photo" role="img" aria-label="Photo of a wooden gavel, brass scales of justice and law books on a desk"></div>
  <div class="hero-shade"></div>
  <h1 class="hero-title"><span class="accent">ACCIDENT?</span> INJURED?</h1>
  <p class="hero-call">Call Us : 555-014-2290</p>
  <svg class="hero-call-btn" width="44" height="44" viewBox="0 0 44 44" aria-label="Call">
    <circle cx="22" cy="22" r="20.5" fill="none" stroke="#fff" stroke-width="2"/>
    <path fill="#fff" d="M16.5 19.8a13 13 0 0 0 7.7 7.7l2.3-2.2c.3-.3.6-.3.9-.2 1 .3 1.9.5 2.9.5.4 0 .7.3.7.7v3c0 .4-.3.7-.7.7A15.4 15.4 0 0 1 12.9 12.7c0-.4.3-.7.7-.7h3c.4 0 .7.3.7.7 0 1 .2 2 .5 2.9.1.3 0 .7-.2.9z"/>
  </svg>
</section>

<section class="features abs">
  <div class="feature" style="left:53px;">
    <svg width="38" height="40" viewBox="0 0 38 40" aria-hidden="true">
      <path d="M19 2 2 16h34z" fill="none" stroke="#34a7d7" stroke-width="2"/>
      <circle cx="19" cy="22" r="9" fill="#34a7d7"/>
      <text x="19" y="27" text-anchor="middle" font-family="Arimo, sans-serif" font-weight="700" font-size="13" fill="#fff">$</text>
      <rect x="4" y="34" width="30" height="2" fill="#34a7d7"/><rect x="1" y="38" width="36" height="2" fill="#34a7d7"/>
    </svg>
  </div>
  <div class="feature-title abs" style="left:53px;top:87px;">Low Fees</div>
  <div class="feature-text abs" style="left:53px;top:117px;width:150px;">We charge less, so you keep more.</div>
  <div class="divider" style="left:212px;"></div>

  <div class="feature" style="left:227px;">
    <svg width="46" height="42" viewBox="0 0 46 42" aria-hidden="true">
      <path d="M12 2h31v22h-6" fill="none" stroke="#34a7d7" stroke-width="2.2"/>
      <path d="M3 9h31v21H14l-7 7v-7H3z" fill="none" stroke="#34a7d7" stroke-width="2.2" stroke-linejoin="round"/>
      <circle cx="12" cy="19.5" r="2" fill="#34a7d7"/><circle cx="18.5" cy="19.5" r="2" fill="#34a7d7"/><circle cx="25" cy="19.5" r="2" fill="#34a7d7"/>
    </svg>
  </div>
  <div class="feature-title abs" style="left:233px;top:88px;">Free Consultation</div>
  <div class="feature-text abs" style="left:231px;top:121px;width:150px;">It's always free to talk to us.</div>
  <div class="divider" style="left:391px;"></div>

  <div class="feature" style="left:402px;">
    <svg width="38" height="42" viewBox="0 0 38 42" aria-hidden="true">
      <path fill="#34a7d7" d="M8 8c-4 3-4 9 0 17s12 15 17 15c3 0 5-1 6-3l-6-7-4 3c-3-2-7-7-8-10l3-4-6-8z"/>
      <path d="M22 8a10 10 0 0 1 9 9M23 3a15 15 0 0 1 13 13" fill="none" stroke="#34a7d7" stroke-width="2" stroke-linecap="round"/>
    </svg>
  </div>
  <div class="feature-title abs" style="left:407px;top:87px;width:165px;">Get Started Using Only Your Phone</div>
  <div class="feature-text abs" style="left:408px;top:121px;width:165px;">No need to come to the office, sign up using your phone.</div>
  <div class="divider" style="left:578px;"></div>

  <div class="feature" style="left:591px;">
    <svg width="48" height="34" viewBox="0 0 48 34" aria-hidden="true">
      <circle cx="8" cy="6" r="5" fill="#34a7d7"/><circle cx="40" cy="6" r="5" fill="#34a7d7"/>
      <path fill="#34a7d7" d="M1 14h12l9 10h-5l-5-5v14H1zM47 14H35l-9 10h5l5-5v14h11z"/>
    </svg>
  </div>
  <div class="feature-title abs" style="left:590px;top:85px;width:165px;">Speak Directly To A Lawyer</div>
  <div class="feature-text abs" style="left:590px;top:121px;width:165px;">No staff screening. Talk right to a lawyer on your first call.</div>

  <div class="rule abs"></div>
  <h2 class="case-title abs">YOUR CASE YOUR MONEY</h2>
  <p class="case-call abs">Call Us : 555-014-2290</p>
  <a class="learn-more abs">LEARN MORE</a>
</section>

<section class="cards abs">
  <article class="card" style="left:52px;">
    <div class="card-media client" role="img" aria-label="Photo of a thoughtful woman seated at a table">
      <h3 class="card-heading">No Fee Unless We<br>Win</h3>
    </div>
    <p class="card-text">We don't get paid unless you get paid. It's as simple as that. We let our results do the talking for us.</p>
  </article>
  <article class="card" style="left:406px;">
    <div class="card-media team" role="img" aria-label="Photo of a group of attorneys in business suits">
      <h3 class="card-heading">Questions About<br>Anything?</h3>
    </div>
    <p class="card-text">We're here to help. Feel free to call us at 555-014-2290 to speak to one of our attorneys. With extensive experience in helping..</p>
  </article>
  <p class="cards-call abs"><span>Call Us :</span> 555-014-2290</p>
</section>

<footer class="site-footer abs">
  <div class="footer-label abs">CONTACT US</div>
  <div class="footer-ring abs" style="left:52px;top:51px;">
    <svg width="14" height="20" viewBox="0 0 14 20" aria-hidden="true"><path fill="#34a7d7" d="M7 0a7 7 0 0 0-7 7c0 5 7 13 7 13s7-8 7-13a7 7 0 0 0-7-7zm0 9.5A2.5 2.5 0 1 1 7 4.5a2.5 2.5 0 0 1 0 5z"/></svg>
  </div>
  <address class="footer-address abs" style="font-style:normal;">Harborline Legal Main Office<br>120 Canal Row Riverton, LA 70000</address>
  <div class="footer-ring abs" style="left:290px;top:51px;">
    <svg width="17" height="17" viewBox="0 0 24 24" aria-hidden="true"><path fill="#34a7d7" d="M6.6 10.8a15.1 15.1 0 0 0 6.6 6.6l2.2-2.2c.3-.3.7-.4 1-.2 1.1.4 2.3.6 3.6.6.6 0 1 .4 1 1V20c0 .6-.4 1-1 1A17 17 0 0 1 3 4c0-.6.4-1 1-1h3.5c.6 0 1 .4 1 1 0 1.3.2 2.5.6 3.6.1.3 0 .7-.2 1z"/></svg>
  </div>
  <div class="footer-phone abs">555-014-2290</div>
  <div class="footer-brand abs">Harborline Legal</div>
  <div class="footer-copy abs">© 2016 <span>Harborline Legal</span> All rights reserved.</div>
</footer>

</body>
</html>
```